Etiketten-Design für Honig
Zielgruppe
Flinker Honig aus dem Bayerischen Wald
Bio
Waldhonig sowie Honig mit Zusätzen wie Bio-Himbeere, Bio-Erdbeere usw.
Aufgabenstellung
Bär, Bayrischer Wald, Bio Nr. und natürlich Honig
Modern und cool

```html
<!DOCTYPE html>
<html lang="de">
<head>
<meta charset="utf-8">
<title>Flinker Honig – Waldhonig Etikett</title>
<link rel="stylesheet" href="https://fonts.googleapis.com/css2?family=Montserrat:wght@600;700;800&family=Josefin+Sans:wght@300&display=swap">
<style>
  :root {
    --frame: #4a2e12;
    --band: #5a3812;
    --cream: #f4e2c8;
    --caramel: #c99a6c;
    --rust: #8a4a22;
    --white: #ffffff;
    --petal-yellow: #f2b233;
    --petal-red: #d4442a;
    --leaf: #5e6a3a;
    --bear: #b57a3c;
  }
  html, body {
    margin: 0;
    padding: 0;
    width: 1200px;
    height: 867px;
    overflow: hidden;
    background: #ffffff;
  }
  .canvas {
    position: relative;
    width: 1200px;
    height: 867px;
    overflow: hidden;
  }
  .label {
    position: absolute;
    left: 186px;
    top: 292px;
    width: 860px;
    height: 364px;
    background: var(--frame);
  }
  .label-art {
    position: absolute;
    left: 6px;
    top: 6px;
    width: 848px;
    height: 352px;
    display: block;
  }
  .text {
    position: absolute;
    margin: 0;
    color: var(--white);
    white-space: nowrap;
  }
  .tagline {
    left: 250px; width: 700px; top: 321px;
    text-align: center;
    font: 700 19px/1 "Montserrat", sans-serif;
    letter-spacing: 0.08em;
    word-spacing: 0.35em;
  }
  .product-name {
    left: 350px; width: 500px; top: 355px;
    text-align: center;
    font: 800 41px/1 "Montserrat", sans-serif;
    letter-spacing: 0.12em;
  }
  .origin {
    left: 419px; width: 400px; top: 561px;
    text-align: center;
    font: 700 23px/1 "Montserrat", sans-serif;
    letter-spacing: 0.06em;
    word-spacing: 0.3em;
  }
  .weight {
    left: 519px; width: 200px; top: 604px;
    text-align: center;
    font: 700 21px/1 "Montserrat", sans-serif;
    letter-spacing: 0.06em;
    word-spacing: 0.25em;
  }
  .info {
    right: 169px;
    text-align: right;
    font: 300 16px/23px "Josefin Sans", sans-serif;
  }
  .producer { top: 386px; }
  .best-before { top: 477px; }
  .lot { top: 545px; }
  .care {
    top: 590px;
    font-size: 12.5px;
    line-height: 18px;
  }
  .warning {
    left: 198px;
    top: 628px;
    font: 300 12.5px/1 "Josefin Sans", sans-serif;
  }
  .photo-credit {
    left: 199px;
    top: 535px;
    font: 300 5px/1 "Josefin Sans", sans-serif;
    transform: rotate(14deg);
    transform-origin: left top;
  }
</style>
</head>
<body>
 <div class="canvas">
  <div class="label">
    <svg class="label-art" viewBox="281 437 1244 516" preserveAspectRatio="none" xmlns="http://www.w3.org/2000/svg">
      <defs>
        <radialGradient id="honeyGlow" cx="900" cy="720" r="700" gradientUnits="userSpaceOnUse">
          <stop offset="0" stop-color="var(--cream)"/>
          <stop offset="0.45" stop-color="var(--caramel)"/>
          <stop offset="1" stop-color="var(--rust)"/>
        </radialGradient>
        <linearGradient id="blossomTones" x1="281" y1="437" x2="1525" y2="800" gradientUnits="userSpaceOnUse">
          <stop offset="0" stop-color="var(--petal-yellow)"/>
          <stop offset="0.25" stop-color="var(--petal-red)"/>
          <stop offset="0.45" stop-color="var(--petal-yellow)"/>
          <stop offset="0.6" stop-color="var(--leaf)"/>
          <stop offset="0.8" stop-color="var(--petal-red)"/>
          <stop offset="1" stop-color="var(--petal-yellow)"/>
        </linearGradient>
        <radialGradient id="bearTone" cx="905" cy="720" r="90" gradientUnits="userSpaceOnUse">
          <stop offset="0" stop-color="#d9a563"/>
          <stop offset="1" stop-color="var(--bear)"/>
        </radialGradient>
      </defs>
      <rect class="honey-field" x="281" y="437" width="1244" height="516" fill="url(#honeyGlow)"/>
      <path class="white-stripe" d="M281,806 C600,850 800,808 960,690 C1100,590 1300,550 1525,544" fill="none" stroke="var(--white)" stroke-width="9"/>
      <path class="brown-band" d="M281,790 C600,834 800,792 960,674 C1100,574 1300,534 1525,530" fill="none" stroke="var(--band)" stroke-width="24"/>
      <path class="flower-photo" role="img" aria-label="Foto: Bienen auf gelb-roten Mädchenaugen-Blüten"
            d="M281,437 H1525 V519 C1300,523 1100,563 952,664 C800,780 600,822 281,779 Z" fill="url(#blossomTones)"/>
      <path class="bear-figure" role="img" aria-label="Illustration: sitzender Comic-Bär"
            d="M860,650 C880,630 945,630 958,660 C975,700 965,735 990,770 C1000,795 960,808 905,806 C850,808 810,795 818,770 C840,735 840,690 860,650 Z"
            fill="url(#bearTone)" stroke="var(--white)" stroke-width="4"/>
    </svg>
  </div>

  <p class="text photo-credit">Photo by Lena M. Hart</p>
  <p class="text tagline">Flinker Honig aus dem Bayerischen Wald</p>
  <h1 class="text product-name">WALDHONIG</h1>

  <div class="text info producer">Flinker Honig<br>Adresse<br>Postleitzahl, Name der Stadt</div>
  <div class="text info best-before">Zumindest eindämmbar<br>bis August 2026</div>
  <div class="text info lot">L2001215</div>

  <p class="text origin">Deutscher Honig</p>
  <p class="text weight">450 g</p>

  <div class="text info care">Honig kann kristallisieren.<br>Erhitzen sie das glas in wasser von max 40°C,<br>dann wird es wieder flussig.</div>
  <p class="text warning">Honig ist nicht für Kinder unter 1 Jahr geeignet.</p>
 </div>
</body>
</html>
```